Innovative cost reduction consultant needs to build a group of technical advisors

We need to share our message and compassion for developing cost reduction in the automotive industry. We create opportunities for immediate innovation, by developing cost reduction solutions across suppliers with related process. Attached is an existing Power Point, but it needs improvement. Most of all, a good compelling story, why experts should join us.

Target Market(s)

Automotive industry, supply chain management

Industry/Entity Type

Automotive

Font styles to use
Serif
Sans Serif

Requirements
Must have
• Better visual graphics. There are a few, but they are not as visually appearing as I would like. A graphic with data should have a better visual impact then the ones that I created. I would like to share the message, that I am providing a solution for the automotive industry. The goal is to reduce costs and improve supplier and OEM relationships. The objective is to do so by creating opportunities for immediate innovation, by developing cost reduction solutions across suppliers with related processes. This message may need a visual graphic, which is missing from the presentation.
Nice to have
• Challenge my story and presentation. Does this make sense to you, and what is your opinions of the subject. Or, a relevant news source to validate the story.
Should not have
• I have not decided on the name of the venture or logo. So, let's just use my name as the source or writer. Marcus Trevell, Cost Reduction Specialist. Thanks,

```html
<!DOCTYPE html>
<html lang="en">
<head>
<meta charset="utf-8">
<title>Cost Reduction Advisory Group – Slide Overview</title>
<link rel="stylesheet" href="https://fonts.googleapis.com/css2?family=Raleway:wght@300;400;600&family=Montserrat:wght@300;400;600&display=swap">
<style>
  :root{
    --navy:#102a5e;
    --navy-deep:#0a1d45;
    --navy-mid:#1a3a78;
    --white:#ffffff;
    --ink:#14264f;
    --mist:#c9d4ea;
    --photo-a:#1c3566;
    --photo-b:#06142f;
    --heat-a:#d6309a;
    --heat-b:#f08a2a;
  }
  *{box-sizing:border-box;margin:0;padding:0}
  html,body{width:855px;height:1200px;overflow:hidden;background:var(--white)}
  body{position:relative;font-family:"Montserrat",Arial,sans-serif;color:var(--white)}
  .slide{position:absolute;width:409px;height:231px;background:var(--navy);overflow:hidden;box-shadow:0 1px 3px rgba(0,0,0,.35)}
  .slide > svg.bg{position:absolute;inset:0;width:100%;height:100%}
  .abs{position:absolute}
  .nowrap{white-space:nowrap}
  .title{position:absolute;left:10px;top:5px;font-family:"Raleway",Arial,sans-serif;font-weight:300;font-size:15px;line-height:16.5px;color:var(--white);padding-left:13px}
  .title.dark{color:var(--ink)}
  .title::before{content:"";position:absolute;left:0;top:3px;width:6px;height:11px;background:currentColor}
  .title::after{content:"";position:absolute;left:8px;top:3px;width:1.5px;height:11px;background:currentColor}
  .page-no{position:absolute;right:18px;bottom:8px;font-size:5px;color:var(--mist)}
  .page-no.dark{color:var(--ink)}
  .photo{position:absolute}
  .box{position:absolute;background:var(--white);color:var(--ink);display:flex;align-items:center;justify-content:center;text-align:center;font-size:6px;line-height:7px}
  .circle{position:absolute;border-radius:50%;background:var(--white);color:var(--ink);display:flex;align-items:center;justify-content:center;text-align:center;font-size:6px;line-height:7px}
  .ticks{position:absolute;list-style:none}
  .ticks li{position:relative;padding-left:30px}
  .ticks li::before{content:"";position:absolute;left:0;top:2px;width:9px;height:9px;border-radius:50%;background:var(--white)}
  .ticks li::after{content:"";position:absolute;left:2.6px;top:3.6px;width:3px;height:4.5px;border:solid var(--navy);border-width:0 1.4px 1.4px 0;transform:rotate(40deg)}
  .small{font-size:5px;line-height:6px}
  .contact-row{position:absolute;left:52px;display:flex;gap:9px;font-size:6.5px;line-height:8px}
  .contact-row svg{flex:none;width:8px;height:8px;fill:var(--white)}
  .pill{position:relative;height:29px;margin-bottom:4px;background:var(--navy);border-radius:14px;padding:0 6px 0 38px;display:flex;align-items:center;justify-content:center;text-align:center}
  .pill .mark{position:absolute;left:0;top:0;width:29px;height:29px;border-radius:50%;background:var(--white);color:var(--navy);font-size:20px;line-height:29px;text-align:center;font-weight:600}
</style>
</head>
<body>

<!-- 1: supplier collaboration -->
<section class="slide" style="left:11px;top:3px">
  <svg class="bg" viewBox="0 0 409 231" aria-hidden="true">
    <polygon points="232,68 244,68 162,231 150,231" fill="#fff" opacity=".9"/>
    <rect x="0" y="162" width="409" height="46" fill="var(--navy-deep)"/>
  </svg>
  <h1 class="title" style="width:390px">Going Beyond Even The Most Advanced Supplier Collaboration And Innovative Models And Inviting Strategic Innovation Opportunities</h1>
  <div class="photo" role="img" aria-label="Line icon of a glowing light bulb" style="left:18px;top:98px;width:42px;height:52px;border-radius:50% 50% 30% 30%;background:radial-gradient(circle at 50% 35%,#ffffff33,#ffffff0a)"></div>
  <div class="box" style="left:65px;top:120px;width:72px;height:22px;clip-path:polygon(0 0,88% 0,100% 50%,88% 100%,0 100%)">Innovative<br>Technology</div>
  <div class="box" style="left:131px;top:110px;width:106px;height:42px;clip-path:polygon(8% 0,100% 0,92% 100%,0 100%)">Forecast data<br>ROI Presentation<br>Identified opportunities<br>Project Planning</div>
  <div class="box" style="left:232px;top:120px;width:90px;height:22px;clip-path:polygon(0 0,90% 0,100% 50%,90% 100%,0 100%,8% 50%)">Opportunities<br>Solutions</div>
  <div class="photo" role="img" aria-label="Red sports car" style="left:328px;top:108px;width:80px;height:42px;border-radius:40% 50% 20% 20%;background:linear-gradient(#e23a3a,#8a1010)"></div>
  <p class="abs nowrap" style="left:42px;top:176px;font-size:9.5px;font-weight:300">Integrating technology providers into the cost improvement strategy</p>
  <span class="page-no">11</span>
</section>

<!-- 2: greater collaboration -->
<section class="slide" style="left:436px;top:3px">
  <div class="photo" role="img" aria-label="Blue-tinted industrial background photo" style="inset:0;background:radial-gradient(circle at 30% 60%,var(--photo-a),var(--photo-b))"></div>
  <svg class="bg" viewBox="0 0 409 231" aria-hidden="true">
    <polygon points="242,52 252,52 200,231 190,231" fill="#fff" opacity=".85"/>
  </svg>
  <h1 class="title" style="width:380px">Collaborating At An Even Greater Level To Achieve Momentous Cost Reduction Goals.</h1>
  <div class="circle" style="left:47px;top:58px;width:48px;height:48px">R&amp;D<br>Industry</div>
  <div class="circle" style="left:17px;top:94px;width:50px;height:50px">Universities</div>
  <div class="circle" style="left:50px;top:130px;width:46px;height:46px">Technical<br>Advisors</div>
  <div class="box" style="left:72px;top:107px;width:90px;height:20px;clip-path:polygon(0 0,90% 0,100% 50%,90% 100%,0 100%)">Innovative Technology</div>
  <div class="box" style="left:180px;top:68px;width:72px;height:68px;clip-path:polygon(12% 0,100% 0,88% 100%,0 100%);font-size:5.5px">Forecast data<br>Identified<br>opportunities<br>ROI Presentation<br>Project Planning</div>
  <div class="box" style="left:150px;top:138px;width:100px;height:86px;clip-path:polygon(14% 0,100% 0,86% 100%,0 100%);font-size:5px;line-height:6px">Solution Categories:<br>Raw Materials<br>Material processing<br>Machining<br>Assembly<br>Packaging / Transportation<br>Tooling &amp; Capital<br>Inspection &amp; Testing</div>
  <div class="box" style="left:243px;top:108px;width:78px;height:22px;clip-path:polygon(0 0,90% 0,100% 50%,90% 100%,0 100%,8% 50%)">Opportunities<br>Solutions</div>
  <div class="circle" style="left:334px;top:88px;width:62px;height:62px;font-size:9px;line-height:10px">Supplier<br>Group</div>
  <span class="page-no">12</span>
</section>

<!-- 3: divider -->
<section class="slide" style="left:11px;top:243px">
  <div class="photo" role="img" aria-label="Grinding wheel throwing blue sparks in a dark workshop" style="inset:0;background:radial-gradient(circle at 40% 40%,#2a4a85,#0a1a3a 75%)"></div>
  <p class="abs" style="right:20px;top:208px;transform:translateY(-100%);text-align:right;font-family:'Raleway',Arial,sans-serif;font-weight:300;font-size:14.5px;line-height:18px">This is Your Divider Page,<br>Place Your Title Here</p>
</section>

<!-- 4: best practices -->
<section class="slide" style="left:436px;top:243px">
  <svg class="bg" viewBox="0 0 409 231" aria-hidden="true">
    <polygon points="270,0 409,0 409,231 60,231" fill="var(--navy-mid)" opacity=".45"/>
    <polygon points="272,0 284,0 256,42 244,42" fill="#fff" opacity=".85"/>
    <polygon points="190,210 202,210 194,231 182,231" fill="#fff" opacity=".85"/>
  </svg>
  <h1 class="title" style="width:225px">Best Practices, Collaborative Effort</h1>
  <ul class="ticks" style="left:28px;top:62px;font-weight:300;font-size:11px;line-height:15.7px">
    <li style="line-height:11px;margin-bottom:8px;width:370px">Incorporating best practices and shared success, supplier groups can achieve momentous cost reduction</li>
    <li>Raw Materials</li>
    <li>Material processing</li>
    <li>Tooling &amp; Capital</li>
    <li>Machining</li>
    <li>Assembly</li>
    <li>Packaging / Transportation</li>
    <li>Inspection &amp; Testing</li>
  </ul>
</section>

<!-- 5: project example -->
<section class="slide" style="left:11px;top:483px">
  <svg class="bg" viewBox="0 0 409 231" aria-hidden="true">
    <polygon points="261,0 274,0 252,36 239,36" fill="#fff" opacity=".85"/>
  </svg>
  <h1 class="title nowrap">Project Example, New Material</h1>
  <p class="abs nowrap" style="left:9px;top:42px;font-size:5.5px">Heater Element and Insulation Material Retrofit Kit Development</p>
  <div class="abs" style="left:6px;top:51px;width:98px;height:162px;background:var(--white)"></div>
  <p class="abs nowrap" style="left:27px;top:54px;color:var(--ink);font-size:5.5px;font-weight:600">Existing material</p>
  <p class="abs nowrap" style="left:27px;top:67px;color:var(--ink);font-size:5.5px">Brick insulation</p>
  <div class="photo" role="img" aria-label="Brick insulation samples" style="left:10px;top:81px;width:91px;height:32px;background:linear-gradient(90deg,#c9c0b8,#eee3c8)"></div>
  <div class="photo" role="img" aria-label="Regional map of generator locations" style="left:21px;top:118px;width:72px;height:78px;background:linear-gradient(135deg,#9fb7d9,#b0c98f)"></div>
  <p class="abs nowrap" style="left:20px;top:199px;color:var(--ink);font-size:4.5px">RX Generator Locations</p>
  <svg class="abs" style="left:107px;top:99px" width="16" height="8" aria-hidden="true"><rect x="0" y="2" width="9" height="4" fill="#fff"/><polygon points="9,0 16,4 9,8" fill="#fff"/></svg>
  <p class="abs nowrap" style="left:136px;top:55px;font-size:5.5px;font-weight:600">Energy savings material</p>
  <p class="abs nowrap" style="left:131px;top:68px;font-size:5.5px">Ceramic fiber insulation</p>
  <div class="photo" role="img" aria-label="Ceramic fiber insulation samples" style="left:128px;top:81px;width:97px;height:32px;background:linear-gradient(90deg,#a07070,#e6e8ee)"></div>
  <p class="abs nowrap" style="left:261px;top:50px;font-size:5px"><b style="font-size:7.5px">40</b> Installations, one engineered solution</p>
  <p class="abs nowrap" style="left:249px;top:69px;font-size:5px"><b style="font-size:7.5px">22%</b> Energy reduction per install</p>
  <p class="abs nowrap" style="left:233px;top:90px;font-size:5px;font-weight:600"><b style="font-size:7.5px">$1.8M</b> Savings impact on supplier group</p>
  <div class="abs" style="left:128px;top:118px;width:162px;height:103px;background:var(--white)"></div>
  <div class="photo" role="img" aria-label="Thermal images before and after the material change" style="left:131px;top:122px;width:156px;height:60px;background:linear-gradient(90deg,var(--heat-a),var(--heat-b) 35%,#fff 42%,#fff 58%,var(--heat-a) 64%,var(--heat-b))"></div>
  <div class="photo" role="img" aria-label="Generator equipment photos" style="left:137px;top:186px;width:128px;height:32px;background:linear-gradient(90deg,#5a6470,#c8cdd3 45%,#c8cdd3 55%,#4c5560)"></div>
  <span class="page-no">15</span>
</section>

<!-- 6: leveraging best practices -->
<section class="slide" style="left:436px;top:483px;background:var(--white)">
  <svg class="bg" viewBox="0 0 409 231" aria-hidden="true">
    <rect x="0" y="42" width="409" height="166" fill="var(--navy)"/>
  </svg>
  <div class="photo" role="img" aria-label="Close-up of meshing machine gears" style="left:0;top:42px;width:250px;height:189px;clip-path:polygon(0 0,62% 0,34% 42%,100% 100%,0 100%);background:radial-gradient(circle at 30% 50%,#d5d5d5,#3a3a3a 70%)"></div>
  <h1 class="title dark" style="width:230px">One Example, And Many Others</h1>
  <p class="abs nowrap" style="left:150px;top:97px;font-family:'Raleway',Arial,sans-serif;font-weight:300;font-size:18px">Leveraging best practices</p>
  <span class="page-no dark">16</span>
</section>

<!-- 7: project planning venn -->
<section class="slide" style="left:11px;top:723px">
  <svg class="bg" viewBox="0 0 409 231" aria-hidden="true">
    <polygon points="0,0 273,0 245,45 0,45" fill="#fff"/>
    <polygon points="0,212 175,212 165,231 0,231" fill="#fff" opacity=".85"/>
    <g fill="#fff">
      <circle cx="282" cy="82" r="50" opacity=".28"/>
      <circle cx="246" cy="132" r="50" opacity=".22"/>
      <circle cx="318" cy="132" r="50" opacity=".22"/>
      <circle cx="282" cy="175" r="50" opacity=".16"/>
    </g>
    <ellipse cx="282" cy="128" rx="26" ry="8" fill="#fff"/>
    <ellipse cx="282" cy="128" rx="7" ry="30" fill="#fff"/>
  </svg>
  <h1 class="title dark" style="width:215px;top:4px">Project Planning, Forecast Data, ROI, GAP Analysis</h1>
  <ul class="ticks" style="left:16px;top:51px;font-size:7px;line-height:7px;width:180px">
    <li style="padding-left:13px;margin-bottom:6px">The products and services provided will support cost reduction objectives.</li>
    <li style="padding-left:13px;margin-bottom:6px">Which includes, a proven mathematical methodology for preparing ROI proposals.</li>
    <li style="padding-left:13px">Example:</li>
  </ul>
  <p class="abs" style="left:47px;top:121px;width:150px;font-size:6.5px;line-height:6.5px">Using a variety of research methodologies, and applied best practices we can provide support in the following areas:</p>
  <p class="abs" style="left:55px;top:151px;font-size:5.5px;line-height:9px">Identified opportunities<br>ROI presentation<br>Project planning</p>
  <p class="abs nowrap" style="left:257px;top:70px;font-size:7px;font-weight:600">Forecast data</p>
  <p class="abs" style="left:210px;top:123px;font-size:7px;font-weight:600;text-align:center;line-height:8px">Project<br>planning</p>
  <p class="abs" style="left:322px;top:118px;font-size:7px;font-weight:600;text-align:center;line-height:9px">ROI<br>presentation</p>
  <p class="abs" style="left:266px;top:125px;font-size:5px;color:var(--ink)">Innovation</p>
  <p class="abs nowrap" style="left:258px;top:180px;font-size:7px;font-weight:600">GAP Analysis</p>
  <span class="page-no">17</span>
</section>

<!-- 8: data analytics -->
<section class="slide" style="left:436px;top:723px">
  <svg class="bg" viewBox="0 0 409 231" aria-hidden="true">
    <polygon points="270,0 284,0 250,60 236,60" fill="#fff" opacity=".85"/>
    <path d="M224,70 v10 h8" stroke="#fff" stroke-width="3" fill="none"/>
    <path d="M264,100 v14 h8" stroke="#fff" stroke-width="3" fill="none"/>
  </svg>
  <h1 class="title">Data Analytics</h1>
  <div class="photo" role="img" aria-label="Stacked spreadsheet screenshots of forecast data" style="left:66px;top:52px;width:150px;height:80px;background:linear-gradient(135deg,#f5f5f5,#d8d8d8 50%,#b8b8b8)"></div>
  <div class="box" style="left:222px;top:48px;width:36px;height:22px;border-radius:4px;font-size:7px">Survey</div>
  <p class="abs small" style="left:262px;top:56px">Effort</p>
  <div class="box" style="left:256px;top:80px;width:50px;height:24px;border-radius:4px;font-size:7px">Forecast<br>data</div>
  <p class="abs small nowrap" style="left:310px;top:90px">Events &amp; timing</p>
  <div class="box" style="left:274px;top:117px;width:34px;height:20px;border-radius:4px;font-size:6.5px">ROI</div>
  <p class="abs small" style="left:313px;top:124px">Solutions</p>
  <p class="abs" style="left:134px;top:155px;font-weight:600;white-space:nowrap"><span style="font-size:30px">$</span> <span style="font-size:27px">$</span> <span style="font-size:24px">$</span> <span style="font-size:20px">$</span> <span style="font-size:17px">$</span> <span style="font-size:14px">$</span> <span style="font-size:11px">$</span> <span style="font-size:7px;margin-left:4px">Piece Price Reduction</span></p>
  <div class="box" style="left:130px;top:197px;width:140px;height:20px;justify-content:space-around;font-size:7px;clip-path:polygon(0 0,92% 0,100% 50%,92% 100%,0 100%)"><span>2010</span><span>6-Year forecast</span><span>2016</span></div>
  <svg class="abs" style="left:268px;top:197px" width="14" height="20" aria-hidden="true"><polyline points="3,2 11,10 3,18" stroke="#fff" stroke-width="3" fill="none"/></svg>
  <div class="photo" role="img" aria-label="Red sports car" style="left:72px;top:196px;width:54px;height:26px;border-radius:40% 50% 20% 20%;background:linear-gradient(#e23a3a,#8a1010)"></div>
  <div class="photo" role="img" aria-label="White sedan" style="left:290px;top:186px;width:80px;height:36px;border-radius:40% 50% 20% 20%;background:linear-gradient(#ffffff,#a9b2bf)"></div>
</section>

<!-- 9: next step -->
<section class="slide" style="left:11px;top:963px;background:var(--white)">
  <div class="photo" role="img" aria-label="Welder working amid sparks" style="left:200px;top:0;width:209px;height:231px;clip-path:polygon(30% 0,100% 0,100% 100%,0 100%);background:radial-gradient(circle at 60% 60%,#3b5f96,#0a1428 70%)"></div>
  <svg class="bg" viewBox="0 0 409 231" aria-hidden="true">
    <polygon points="0,50 305,50 265,190 0,190" fill="var(--navy)"/>
  </svg>
  <h1 class="title dark">Next Step</h1>
  <ul class="ticks" style="left:19px;top:84px;font-size:11.5px;line-height:17.3px;font-weight:300;white-space:nowrap">
    <li style="padding-left:17px">Build advisor group</li>
    <li style="padding-left:17px">Proposal for Kestrel Motors</li>
    <li style="padding-left:17px">Marcus's relationship with Kestrel Motors NAP</li>
    <li style="padding-left:17px">Meeting with Kestrel Motors R&amp;D purchasing</li>
  </ul>
  <span class="page-no">19</span>
</section>

<!-- 10: join us -->
<section class="slide" style="left:436px;top:963px">
  <div class="photo" role="img" aria-label="Dark industrial gear and machinery background" style="inset:0;background:radial-gradient(circle at 60% 45%,#3a4f6b,#0b1522 75%)"></div>
  <div class="abs" style="left:40px;top:0;width:179px;height:231px;background:var(--navy);opacity:.94"></div>
  <div class="abs" style="left:40px;top:203px;width:179px;height:28px;background:var(--navy-mid)"></div>
  <p class="abs" style="left:60px;top:26px;font-family:'Raleway',Arial,sans-serif;font-weight:300;font-size:29px">Join Us!</p>
  <p class="abs" style="left:60px;top:84px;font-size:11px;font-weight:300;border-bottom:1px solid #fff;padding-bottom:3px;width:130px">Contact Information</p>

  <div class="contact-row" style="top:128px">
    <svg viewBox="0 0 8 8" aria-hidden="true"><circle cx="4" cy="2.2" r="2"/><path d="M0.5,8 q3.5,-5 7,0z"/></svg>
    <span>Marcus Trevell</span>
  </div>
  <div class="contact-row" style="top:143px">
    <svg viewBox="0 0 8 8" aria-hidden="true"><path d="M4,0.5 L8,4 H6.8 V7.5 H1.2 V4 H0z"/></svg>
    <span>218 Harbor Ln<br>Westfield, OH 44010</span>
  </div>
  <div class="contact-row" style="top:170px">
    <svg viewBox="0 0 8 8" aria-hidden="true"><path d="M1,0.5 l2,0 0.6,2 -1.2,1 q1,2 2.6,2.6 l1,-1.2 2,0.6 0,2 q-5,0.4 -7,-7z"/></svg>
    <span>+1 (555) 014-2290</span>
  </div>
  <div class="contact-row" style="top:189px">
    <svg viewBox="0 0 8 8" aria-hidden="true"><rect x="0.5" y="1.5" width="7" height="5"/></svg>
    <span>Marcus.Trevell@northlanecr.com</span>
  </div>

  <div class="abs" style="left:106px;top:212px;display:flex;gap:8px">
    <span style="width:10px;height:10px;border-radius:50%;background:#fff"></span>
    <span style="width:10px;height:10px;border-radius:50%;background:#fff"></span>
    <span style="width:10px;height:10px;border-radius:50%;background:#fff"></span>
  </div>
  <div class="abs" style="left:268px;top:137px;width:137px;font-size:5px;line-height:6px">
    <div class="pill"><span class="mark">!</span>Our Purpose is to fund innovation through mutual benefits.</div>
    <div class="pill"><span class="mark">!</span>Our Objective is the alignment of cost reduction Technology and cost improvement requirements.</div>
    <div class="pill" style="margin-bottom:0"><span class="mark">!</span>Our Mission is to provide new market opportunities.</div>
  </div>
</section>

</body>
</html>
```